Business Card for Modern Marketing Consultancy

Business card needed for marketing consultancy with existing logo.

Lanternway Co is a specialized boutique marketing consultancy that provides startup, small and mid size consumer businesses thought leadership and implementation of marketing strategies to help your business grow.

Our expertise, experience and industry knowledge stems from some of New York’s top global beauty and retail companies and allows us to draw from an array of successful marketing strategies and growth tactics tailored to suit the needs of your business

lanternwayco.example

Target Market(s)

start up, small and mid size consumer packaged goods businesses

Industry/Entity Type

Leadership

Requirements
Must have
• Must have the logo of the business and use of the exact colors of the logo.
Must be simple, sleek, modern and clean. Must make a statement and be eye catching.

Front: looking for unique design or visual statement with logo and tagline

Back of card should have:
logo - if not use on front.
Delia R. Horvath
Founder
Lanternway Co
m: 555.014.2276
deliahorvath@lanternwayco.example
lanternwayco.example

Please use the following words as these describe my services:
strategy analytics branding research

Please refer to the website look and feel: lanternwayco.example

Please kindly note that I am looking for a unique design that I cannot do myself with a template. thank you.
Nice to have
• Please also try and incorporate additional files attached.

```html
<!DOCTYPE html>
<html lang="en">
<head>
<meta charset="utf-8">
<title>Lanternway Co — Business Card</title>
<link rel="stylesheet" href="https://fonts.googleapis.com/css2?family=Questrial&display=swap">
<style>
  :root {
    --magenta: #b3176a;
    --ink: #5a5a5e;
    --ink-dark: #3f3f42;
    --card-dark: #3a3a3b;
    --url-light: #c9c9cb;
    --paper: #ffffff;
    --band-gray: #6a6a6d;
    --backdrop: #e6e4e1;
  }
  * { box-sizing: border-box; margin: 0; padding: 0; }
  html, body {
    width: 1200px; height: 871px; overflow: hidden;
    background: var(--backdrop);
    font-family: "Questrial", "Century Gothic", sans-serif;
  }
  .stage { position: relative; width: 1200px; height: 871px; }
  .card {
    position: absolute; left: 300px; width: 600px; height: 343px;
    border-radius: 3px; overflow: hidden;
    box-shadow: 0 6px 18px rgba(0,0,0,0.18);
  }
  /* Card back */
  .card-back { top: 68px; background: var(--card-dark); }
  .back-mark {
    position: absolute; top: 118px; left: 0; right: 0;
    display: flex; align-items: center; justify-content: center; gap: 14px;
  }
  .mark-dot { width: 22px; height: 22px; border-radius: 50%; background: var(--magenta); }
  .back-name { color: var(--magenta); font-size: 40px; letter-spacing: -0.5px; }
  .back-url {
    position: absolute; top: 232px; left: 0; right: 0; text-align: center;
    color: var(--url-light); font-size: 19px; letter-spacing: 0.3px;
  }
  /* Card front */
  .card-front { top: 460px; background: var(--paper); }
  .brand {
    position: absolute; top: 34px; left: 40px;
    display: flex; align-items: center; gap: 14px;
  }
  .brand-name { color: var(--ink); font-size: 56px; letter-spacing: -1.5px; line-height: 1; }
  .tagline {
    position: absolute; top: 100px; left: 44px;
    color: var(--magenta); font-size: 19px; letter-spacing: 0.4px;
  }
  .person { position: absolute; top: 168px; left: 58px; }
  .person-name { color: var(--ink-dark); font-size: 15px; font-weight: 700; letter-spacing: 0.3px; }
  .person-role { color: var(--magenta); font-size: 14px; margin-top: 9px; }
  .contacts { position: absolute; top: 196px; left: 300px; list-style: none; }
  .contacts li {
    display: flex; align-items: center; gap: 16px;
    color: var(--ink); font-size: 14px; height: 26px;
  }
  .contacts svg { width: 13px; height: 13px; flex: none; }
  .icon-fill { fill: var(--magenta); }
  .icon-line { fill: none; stroke: var(--magenta); stroke-width: 1.4; }
  .band { position: absolute; bottom: 0; }
  .band-gray { left: 0; width: 240px; height: 11px; background: var(--band-gray); }
  .band-magenta { left: 240px; right: 0; height: 14px; background: var(--magenta); }
</style>
</head>
<body>
<main class="stage">
  <section class="card card-back" aria-label="Card back">
    <div class="back-mark">
      <span class="mark-dot"></span>
      <span class="back-name">Lanternway Co</span>
    </div>
    <p class="back-url">lanternwayco.example</p>
  </section>

  <section class="card card-front" aria-label="Card front">
    <div class="brand">
      <span class="brand-name">Lanternway Co</span>
      <span class="mark-dot"></span>
    </div>
    <p class="tagline">brighter paths for your brand</p>

    <div class="person">
      <p class="person-name">Delia R. Horvath</p>
      <p class="person-role">Founder</p>
    </div>

    <ul class="contacts">
      <li>
        <svg viewBox="0 0 16 16" aria-hidden="true"><path class="icon-fill" d="M3 2h3l1.5 3.5-2 1.3a9 9 0 0 0 3.7 3.7l1.3-2L14 10v3a1 1 0 0 1-1 1A12 12 0 0 1 2 3a1 1 0 0 1 1-1z"/></svg>
        555.014.2276
      </li>
      <li>
        <svg viewBox="0 0 16 16" aria-hidden="true"><path class="icon-fill" d="M1 3h14v10H1z M2.5 4.5 8 8.8l5.5-4.3V4.3L8 7.6 2.5 4.3z" fill-rule="evenodd"/></svg>
        deliahorvath@lanternwayco.example
      </li>
      <li>
        <svg viewBox="0 0 16 16" aria-hidden="true"><g class="icon-line"><circle cx="8" cy="8" r="6.5"/><ellipse cx="8" cy="8" rx="2.8" ry="6.5"/><path d="M1.5 8h13M2.5 4.8h11M2.5 11.2h11"/></g></svg>
        lanternwayco.example
      </li>
    </ul>

    <div class="band band-gray"></div>
    <div class="band band-magenta"></div>
  </section>
</main>
</body>
</html>
```